Inspirational quotes poster shop seeks poster designs

Hi! We are launching an eshop with design posterss featuring inspirational quotes. We need a first poster design while looking for further cooperation on around 20 poster designs. We need outputs in the format that can go to high quality print (size at least 100x70cm).

For the first design feel free to choose any of the following quotes to depict:

1. "Stop starting. Start finishing." Author: Tobias Wrennholt, Plinkora
2. "A problem well stated is a problem half solved." Author: Walter J. Brimsley, American inventor
3. "The best way to predict the future is to invent it." Author: Frank Dolan, Quince

Designs should be rarther simple, think please of your whole concept and how various posters would go together. Every poster can be quite different though, in terms of fonts, colours and overall design, together they should however form and interesting collage.

Designs must contain the quote, author & company. it can be pure text or some indication of the sense of the quote.

Design must also feature company name/logo (not available yet, for now please use "brainvolter" as a working name), QR code with a title "Read the story"

See these posters for design we like (for inspiration ONLY!):
http://www.foundertonics.example/products/founder-print-its-simple-until-you-make-it-complicated
http://www.foundertonics.example/products/founder-print-marcus-pellway-less-meetings-more-doing
http://www.foundertonics.example/products/founder-print-lionel-habberg-stop-sketching-start-building
Updates

Hi to everybody! Sorry for the spam, some of you have been struggling with finding the crux in the quote, so here I offer some ideas what to look for in them. It's up to you to take it, leave it or change it:)

Stop starting, start finishing -
1 - stop starting with many times repeated small word starting, perhaps large word starting made of small words starting, with it contrasting start finishing in normal bold font.
2 - STARTING could look quite unfinished, sketchy, especially -ING could look more unfinished then the rest , e.g. just rough indication of outline of the letters, again contrasting with start finishing will clean & neat writting.

Problem well stated is a problem half solved - look for something that is clearer by defining the problem. Perhaps in a simple sketch like here http://www.foundertonics.example/products/founder-print-its-simple-until-you-make-it-complicated  point out a route from a problem (light = flame), to a solution (lightbulb, lightbulb design drawing or something like that).

Anyway, despite preference for simple design, I am still looking for some smart, creative, catchy idea in the design. Check with yourself if it's something you can would want to buy and hang up on your wall.

Good luck to all of you and again, thank you all very much for participation!
Radim

Target Market(s)

businesses of every size, from startups to large corporates seeking culture change or motivation kick up

Industry/Entity Type

Shop

Requirements
Must have
• I strongly prefer portrait orientation of the poster!

Nice to have
• Quotes themselves are often on the edge, teasing, so the design can be.
Should not have
• Try to avoid traditional dialoge bubble for the quote itself as the first obvious idea for depicting a quote.

Avoid using photos (not simple then) or too many colours.

Of course, by no means use a COPY of existing designs I linked to for inspiration. It just shows what we like.

```html
<!DOCTYPE html>
<html lang="en">
<head>
<meta charset="utf-8">
<title>Stop Starting, Start Finishing – Poster</title>
<link rel="stylesheet" href="https://fonts.googleapis.com/css2?family=Source+Sans+3:wght@400;600;700&display=swap">
<style>
  :root {
    --bg-teal: #2e9c98;
    --brand-teal: #1d6e6a;
    --ink: #0b0f0f;
    --paper: #ffffff;
    --qr-fill: #e9f4f3;
  }
  html, body {
    margin: 0;
    padding: 0;
    width: 840px;
    height: 1200px;
    overflow: hidden;
  }
  .poster {
    position: relative;
    width: 840px;
    height: 1200px;
    background: var(--bg-teal);
    overflow: hidden;
    font-family: "Source Sans 3", "Myriad Pro", sans-serif;
  }
  .brand-name {
    position: absolute;
    top: 60px;
    left: 0;
    width: 100%;
    margin: 0;
    text-align: center;
    font-size: 24px;
    font-weight: 600;
    letter-spacing: 0.5px;
    color: var(--brand-teal);
  }
  .starting-line {
    position: absolute;
    margin: 0;
    white-space: nowrap;
    font-size: 64px;
    line-height: 1;
    font-weight: 400;
    color: var(--ink);
  }
  .starting-line--first { top: 322px; left: 17px; }
  .starting-line--second { top: 404px; left: -36px; }
  .starting-line--third { top: 486px; left: 12px; }
  .stop-word { font-weight: 700; }
  .headline {
    margin: 0;
    font-weight: normal;
  }
  .headline__start {
    position: absolute;
    top: 526px;
    left: 80px;
    font-size: 200px;
    line-height: 1;
    font-weight: 600;
    color: var(--paper);
  }
  .headline__finish {
    position: absolute;
    top: 707px;
    left: 84px;
    font-size: 100px;
    line-height: 1;
    font-weight: 700;
    letter-spacing: 3px;
    color: var(--ink);
  }
  .attribution {
    position: absolute;
    top: 993px;
    left: 371px;
    width: 347px;
    margin: 0;
    border-top: 2px solid var(--ink);
    padding-top: 10px;
    text-align: center;
    font-size: 24px;
    color: var(--ink);
  }
  .attribution__author { font-weight: 700; }
  .story-link {
    position: absolute;
    left: 86px;
    top: 1000px;
    width: 104px;
    text-align: center;
  }
  .story-link__title {
    margin: 0 0 8px;
    font-size: 16px;
    font-weight: 600;
    color: var(--ink);
    white-space: nowrap;
  }
  .story-link__code {
    display: block;
    width: 104px;
    height: 104px;
  }
</style>
</head>
<body>
  <main class="poster">
    <p class="brand-name">BRAINVOLTER</p>

    <p class="starting-line starting-line--first"><span class="stop-word">STOP</span> STARTING, STARTING, STARTING,</p>
    <p class="starting-line starting-line--second">STARTING, STARTING, STARTING, STARTING,</p>
    <p class="starting-line starting-line--third">STARTING, STARTING, STARTING, STARTING,</p>

    <h1 class="headline">
      <span class="headline__start">START</span>
      <span class="headline__finish">FINISHING.</span>
    </h1>

    <p class="attribution"><span class="attribution__author">Tobias Wrennholt,</span> Plinkora</p>

    <div class="story-link">
      <p class="story-link__title">Read the story</p>
      <svg class="story-link__code" viewBox="0 0 104 104" role="img" aria-label="QR code linking to the story behind the quote">
        <rect x="1" y="1" width="102" height="102" fill="var(--qr-fill)" stroke="var(--ink)" stroke-width="2"/>
      </svg>
    </div>
  </main>
</body>
</html>
```